DL Cards to get buyers attention

I’m looking to have four double-sided DL flyers professionally prepared and made print-ready in high resolution.

I have uploaded the four existing designs, and I’m happy for them to be reviewed with a fresh set of eyes. While I’m generally happy with the direction, I’m very open to recommendations around layout, typography, imagery, colour balance, spacing and overall presentation if there are opportunities to create a stronger and more professional result.

The key objective is to develop a consistent and recognisable suite of marketing material that strengthens both Fen Calder brand awareness and my personal profile in the local real estate market. Each flyer should feel like part of the same campaign while still having its own clear message and purpose.

I want the finished designs to feel professional, confident, modern and premium, without becoming overly busy or losing the simplicity that makes a DL flyer easy to read. Strong headlines, clear messaging and an obvious call to action are important. The Fen Calder branding should be immediately recognisable, while my photograph, name and contact details should be incorporated naturally and consistently.

Please review the existing designs and suggest any changes that would improve their visual impact, readability and consistency. I’m also open to seeing an alternative design direction if you believe there is a better overall look.

The final artwork needs to be supplied professionally print-ready at DL size (210 mm × 99 mm), double-sided, high resolution, CMYK where appropriate, with 3 mm bleed and safe margins, so it can be provided directly to a commercial printer.

The overall goal is simple: strong branding, professional presentation, consistent recognition and marketing material that people will remember.

Target Market(s)

People looking at selling their homes

Industry/Entity Type

Real Estate

Font styles to use
Serif
Sans Serif

Requirements
Must have
• Strong brand awareness - Fen Calder
Nice to have
• bright and fresh

```html
<!DOCTYPE html>
<html lang="en">
<head>
<meta charset="utf-8">
<title>Fen Calder – 10 Things to Get Your Property Ready to Sell DL Flyer</title>
<link rel="stylesheet" href="https://fonts.googleapis.com/css2?family=Anton&family=Montserrat:wght@400;500;800&family=Rubik:wght@400;500;700;800&family=Yellowtail&display=swap">
<style>
  :root {
    --brand-yellow: #ffe500;
    --sky-deep: #0b4fd6;
    --sky-light: #3f8ff0;
    --sand: #f3f3f1;
    --accent-blue: #1f8fd0;
    --script-blue: #1f6fae;
    --ink: #2b2b2b;
    --ink-soft: #444;
    --footer-grey: #5a5a5a;
    --page-bg: #cfcfcf;
    --white: #ffffff;
  }
  * { margin: 0; padding: 0; box-sizing: border-box; }
  html, body { width: 1004px; height: 1200px; overflow: hidden; }
  body { background: var(--page-bg); position: relative; font-family: "Rubik", sans-serif; color: var(--ink); }

  .card { position: absolute; left: 80px; width: 844px; height: 410px; overflow: hidden; }
  .card-front { top: 158px; }
  .card-back { top: 633px; background: linear-gradient(90deg, #f1f1f1 0%, #ffffff 45%, #f4f4f4 100%); }

  /* front */
  .hero-photo { position: absolute; inset: 0;
    background: linear-gradient(180deg, var(--sky-deep) 0%, var(--sky-light) 50%, #2fc4cf 53%, #e9f2f2 56%, var(--sand) 100%); }
  .brand-box { position: absolute; left: 705px; top: 0; width: 105px; height: 104px; background: var(--brand-yellow);
    display: flex; align-items: center; justify-content: center; padding-top: 20px; }
  .brand-name { font-family: "Rubik", sans-serif; font-weight: 700; font-size: 15px; color: #3a3a3a; white-space: nowrap; }

  .headline-number { position: absolute; left: 48px; top: 50px; font-family: "Anton", sans-serif; font-size: 176px; line-height: 1; color: var(--brand-yellow); letter-spacing: -6px; transform: scaleX(0.78); transform-origin: left top; }
  .headline-word { position: absolute; left: 168px; top: 52px; font-family: "Anton", sans-serif; font-size: 98px; line-height: 1; color: var(--brand-yellow); transform: scaleX(0.68); transform-origin: left top; }
  .headline-sub { position: absolute; left: 168px; top: 143px; font-family: "Montserrat", sans-serif; font-weight: 400; font-size: 20px; letter-spacing: 7px; color: var(--white); white-space: nowrap; }
  .headline-main { position: absolute; left: 166px; top: 164px; font-family: "Montserrat", sans-serif; font-weight: 800; font-size: 39px; letter-spacing: 10px; color: var(--white); white-space: nowrap; }

  .intro-rule { position: absolute; left: 62px; top: 245px; width: 1.5px; height: 112px; background: var(--accent-blue); }
  .intro-script { position: absolute; left: 92px; top: 242px; font-family: "Yellowtail", "Brush Script MT", cursive; font-size: 42px; line-height: 1.1; color: var(--script-blue); white-space: nowrap; }
  .intro-copy { position: absolute; left: 90px; top: 305px; font-family: "Montserrat", sans-serif; font-size: 13.5px; line-height: 17px; color: var(--ink); }
  .intro-copy strong { font-family: "Rubik", sans-serif; font-weight: 700; color: var(--accent-blue); }
  .web-rule { position: absolute; left: 265px; top: 353px; width: 357px; height: 1px; background: var(--accent-blue); opacity: .6; }
  .web-address { position: absolute; left: 629px; top: 343px; font-family: "Montserrat", sans-serif; font-size: 13.5px; letter-spacing: 3.6px; color: var(--ink); white-space: nowrap; }

  /* back */
  .top-rule { position: absolute; left: 0; top: 11px; width: 726px; height: 1px; background: var(--brand-yellow); }
  .side-band { position: absolute; left: 737px; top: 0; width: 107px; height: 410px; background: var(--brand-yellow); }
  .agent-photo { position: absolute; left: 636px; top: 95px; width: 208px; height: 315px;
    background: linear-gradient(180deg, #c99a7a 0%, #d9b39a 35%, #f2f2f2 55%, #ffffff 100%);
    border-radius: 90px 90px 0 0; }

  .tips { position: absolute; left: 31px; top: 30px; width: 608px; display: grid; grid-template-columns: repeat(5, 1fr); grid-template-rows: 133px 140px; row-gap: 8px; }
  .tip { position: relative; text-align: center; padding: 0 6px; border-bottom: 1px solid var(--brand-yellow); }
  .tip:not(:nth-child(5n)) { border-right: 1px solid var(--brand-yellow); }
  .tip-icon { width: 35px; height: 35px; margin: 0 auto 9px; display: block; }
  .tip-title { font-size: 10px; line-height: 11px; font-weight: 400; color: var(--ink); text-transform: uppercase; }
  .tip-title b { font-weight: 800; display: block; }
  .tip-text { font-size: 8px; line-height: 10.8px; color: var(--ink-soft); margin-top: 5px; }
  .tip-num { position: absolute; right: 0; bottom: -5px; font-weight: 800; font-size: 14px; line-height: 1; color: var(--brand-yellow); background: #fafafa; padding-left: 2px; }

  .footer-band { position: absolute; left: 0; top: 337px; width: 636px; height: 73px; background: var(--footer-grey);
    display: flex; align-items: center; padding-left: 29px; white-space: nowrap; }
  .footer-call { font-family: "Yellowtail", "Brush Script MT", cursive; font-size: 34px; line-height: 1; color: var(--brand-yellow); }
  .footer-phone-icon { width: 24px; height: 24px; margin-left: 12px; flex: none; }
  .footer-phone { margin-left: 10px; font-weight: 800; font-size: 30px; line-height: 1; color: var(--white); letter-spacing: 0.5px; }
  .footer-divider { width: 1px; height: 30px; background: var(--brand-yellow); margin: 0 18px; flex: none; }
  .footer-tag { font-family: "Montserrat", sans-serif; font-size: 13px; line-height: 14px; letter-spacing: 2px; color: var(--white); }
  .footer-tag b { font-weight: 800; }
  .footer-tag .hl { color: var(--brand-yellow); }
</style>
</head>
<body>

<section class="card card-front">
  <div class="hero-photo" role="img" aria-label="Photo of a bright blue sky over a white beach with riders on a line of camels"></div>
  <div class="brand-box"><span class="brand-name">Fen Calder</span></div>
  <div class="headline-number">10</div>
  <div class="headline-word">THINKS</div>
  <div class="headline-sub">TO GET YOUR</div>
  <div class="headline-main">PROPERTY</div>
  <div class="intro-rule"></div>
  <div class="intro-script">Ready to Sell</div>
  <p class="intro-copy">A well-prepared home makes a<br>lasting first impression and helps<br><strong>achieve the best result.</strong></p>
  <div class="web-rule"></div>
  <div class="web-address">www.fencalder.com</div>
</section>

<section class="card card-back">
  <div class="top-rule"></div>
  <div class="side-band"></div>
  <div class="agent-photo" role="img" aria-label="Portrait photo of the agent in a white branded shirt"></div>

  <div class="tips">
    <div class="tip">
      <svg class="tip-icon" viewBox="0 0 36 36" fill="none" stroke="#444" stroke-width="1"><circle cx="18" cy="18" r="16.5" stroke="#ffe500" stroke-width="1.6"/><path d="M14 10l4 10M12 20h10l2 6H10z"/><circle cx="25" cy="12" r="1"/></svg>
      <div class="tip-title">Clean &amp; <b>Declutter</b></div>
      <p class="tip-text">Remove personal items and clutter. A clean, tidy home feels bigger, brighter and more inviting.</p>
      <span class="tip-num">01</span>
    </div>
    <div class="tip">
      <svg class="tip-icon" viewBox="0 0 36 36" fill="none" stroke="#444" stroke-width="1"><circle cx="18" cy="18" r="16.5" stroke="#ffe500" stroke-width="1.6"/><circle cx="18" cy="18" r="6"/><circle cx="18" cy="18" r="2.5"/><path d="M18 9v3M18 24v3M9 18h3M24 18h3M12 12l2 2M22 22l2 2M24 12l-2 2M12 24l2-2"/></svg>
      <div class="tip-title">Finish Projects <b>&amp; Repairs</b></div>
      <p class="tip-text">Fix minor issues, leaky taps, loose handles and any repairs buyers will notice.</p>
      <span class="tip-num">02</span>
    </div>
    <div class="tip">
      <svg class="tip-icon" viewBox="0 0 36 36" fill="none" stroke="#444" stroke-width="1"><circle cx="18" cy="18" r="16.5" stroke="#ffe500" stroke-width="1.6"/><rect x="11" y="10" width="11" height="15"/><circle cx="20" cy="19" r="4"/><path d="M23 22l4 4M13 13h6M13 16h4"/></svg>
      <div class="tip-title">Do a Thorough <b>Inspection</b></div>
      <p class="tip-text">Check the big and small things inside and out so there are no surprises later.</p>
      <span class="tip-num">03</span>
    </div>
    <div class="tip">
      <svg class="tip-icon" viewBox="0 0 36 36" fill="none" stroke="#444" stroke-width="1"><circle cx="18" cy="18" r="16.5" stroke="#ffe500" stroke-width="1.6"/><rect x="12" y="10" width="13" height="5" rx="1"/><path d="M25 12h2v5h-8v3M18 20h2v7h-2z"/></svg>
      <div class="tip-title">Paint</div>
      <p class="tip-text">A fresh coat of neutral paint can transform your home and make it feel well maintained.</p>
      <span class="tip-num">04</span>
    </div>
    <div class="tip">
      <svg class="tip-icon" viewBox="0 0 36 36" fill="none" stroke="#444" stroke-width="1"><circle cx="18" cy="18" r="16.5" stroke="#ffe500" stroke-width="1.6"/><path d="M11 11l14 14M25 11L11 25M10 10l3-1 1 3M26 26l-3 1-1-3"/></svg>
      <div class="tip-title">Freshen Up Fixtures <b>&amp; Hardware</b></div>
      <p class="tip-text">Update old light fittings, tapware and cabinet handles for an instant lift.</p>
      <span class="tip-num">05</span>
    </div>
    <div class="tip">
      <svg class="tip-icon" viewBox="0 0 36 36" fill="none" stroke="#444" stroke-width="1"><circle cx="18" cy="18" r="16.5" stroke="#ffe500" stroke-width="1.6"/><rect x="11" y="11" width="14" height="14"/><path d="M14.5 11v14M18 11v14M21.5 11v14M11 14.5h14M11 18h14M11 21.5h14"/></svg>
      <div class="tip-title">Clean or Replace <b>Flooring</b></div>
      <p class="tip-text">Clean carpets, tiles and floors or replace if needed. Great floors make a big difference.</p>
      <span class="tip-num">06</span>
    </div>
    <div class="tip">
      <svg class="tip-icon" viewBox="0 0 36 36" fill="none" stroke="#444" stroke-width="1"><circle cx="18" cy="18" r="16.5" stroke="#ffe500" stroke-width="1.6"/><path d="M10 26V12M26 26V12M10 16q8-5 16 0M13 26v-9M16 26v-10M20 26v-10M23 26v-9M10 26h16"/></svg>
      <div class="tip-title">Create a Welcoming <b>Entrance</b></div>
      <p class="tip-text">Tidy up the front yard, clean the entry and add plants for great street appeal.</p>
      <span class="tip-num">07</span>
    </div>
    <div class="tip">
      <svg class="tip-icon" viewBox="0 0 36 36" fill="none" stroke="#444" stroke-width="1"><circle cx="18" cy="18" r="16.5" stroke="#ffe500" stroke-width="1.6"/><path d="M10 18l8-7 8 7M12 16v10h12V16M16 26v-5h4v5"/></svg>
      <div class="tip-title">Stage Your <b>Home</b></div>
      <p class="tip-text">Arrange furniture to showcase space and lifestyle. Less is more when selling.</p>
      <span class="tip-num">08</span>
    </div>
    <div class="tip">
      <svg class="tip-icon" viewBox="0 0 36 36" fill="none" stroke="#444" stroke-width="1"><circle cx="18" cy="18" r="16.5" stroke="#ffe500" stroke-width="1.6"/><path d="M13 26q-3-4 0-8t0-8M18 26q-3-4 0-8t0-8M23 26q-3-4 0-8t0-8M11 25l14-14"/></svg>
      <div class="tip-title">Eliminate <b>Odours</b></div>
      <p class="tip-text">Remove pet smells, smoke, cooking and musty odours for a fresh, neutral home.</p>
      <span class="tip-num">09</span>
    </div>
    <div class="tip">
      <svg class="tip-icon" viewBox="0 0 36 36" fill="none" stroke="#444" stroke-width="1"><circle cx="18" cy="18" r="16.5" stroke="#ffe500" stroke-width="1.6"/><path d="M19 10h7v7l-9 9-7-7z"/><circle cx="22.5" cy="13.5" r="1.2"/></svg>
      <div class="tip-title">Get Your Real <b>Price</b></div>
      <p class="tip-text">Work with an agent to set the right price and attract the right buyers.</p>
      <span class="tip-num">10</span>
    </div>
  </div>

  <div class="footer-band">
    <span class="footer-call">Call Jory</span>
    <svg class="footer-phone-icon" viewBox="0 0 24 24"><circle cx="12" cy="12" r="12" fill="#ffe500"/><path d="M8 6.5l2 2.5-1.2 1.6q1.4 2.8 4.6 4.6l1.6-1.2 2.5 2-1.5 2q-6-.5-9.5-9.5z" fill="#5a5a5a"/></svg>
    <span class="footer-phone">0400 555 123</span>
    <span class="footer-divider"></span>
    <span class="footer-tag">YOUR <b>PROPERTY</b><br>OUR <b class="hl">PRIORITY</b></span>
  </div>
</section>

</body>
</html>
```